business card for a massage therapy practice named 'Meadow and Rowan Massage Studio'

I really need a trendy, yet easy on the eyes business card to complement my logo. Ideally with some gold or rose gold foil work.

My uploaded file of the logo I have in horizontal but I have a vertical version as well. Another color that is used in the website is a blush pink here and there. I'd like to see some trendy tropical leaves in the design.

```html
<!DOCTYPE html>
<html lang="en">
<head>
<meta charset="utf-8">
<title>Meadow and Rowan Massage Studio – Business Card</title>
<link rel="stylesheet" href="https://fonts.googleapis.com/css2?family=Amatic+SC:wght@700&family=Questrial&display=swap">
<style>
  :root {
    --backdrop: #e3e3e3;
    --paper: #fdfdfb;
    --gold: #8c7853;
    --gold-text: #9a8257;
    --mint: #82d3bf;
    --mint-soft: #bfe8dd;
    --ink: #4d4d4d;
    --pattern-light: #f1eee6;
  }
  * { box-sizing: border-box; margin: 0; padding: 0; }
  html, body { width: 1200px; height: 857px; overflow: hidden; }
  body {
    background: var(--backdrop);
    font-family: "Questrial", "Century Gothic", sans-serif;
    position: relative;
  }
  .card {
    position: absolute;
    top: 280px;
    width: 520px;
    height: 297px;
    background: var(--paper);
    overflow: hidden;
    box-shadow: 0 6px 18px rgba(0,0,0,0.12);
  }
  .card--back { left: 50px; }
  .card--front { left: 630px; }

  /* back side */
  .back-pattern {
    position: absolute; inset: 0;
    background: linear-gradient(135deg, var(--pattern-light), #ebe6d8 50%, #e6efe6);
  }
  .back-panel {
    position: absolute;
    left: 95px; top: 88px;
    width: 330px; height: 121px;
    background: var(--paper);
    border: 2px solid var(--mint-soft);
    display: flex; align-items: center; justify-content: center; gap: 14px;
  }
  .brand-dot {
    width: 14px; height: 14px; border-radius: 50%;
    background: var(--gold);
    flex: none;
  }
  .brand-name {
    font-family: "Questrial", "Century Gothic", sans-serif;
    font-size: 19px; line-height: 1.25;
    letter-spacing: 0.5px;
    color: var(--ink);
  }

  /* front side */
  .front-pattern {
    position: absolute; left: 0; top: 0; bottom: 0;
    width: 210px;
    background: linear-gradient(160deg, #927e58, var(--gold) 60%, #85724f);
  }
  .front-brand {
    position: absolute;
    left: 22px; top: 104px;
    width: 250px; height: 86px;
    background: var(--mint);
    display: flex; align-items: center; justify-content: center; gap: 10px;
  }
  .front-brand .brand-dot { background: var(--paper); }
  .front-brand .brand-name { color: #1f3a33; font-size: 16px; }

  .contact {
    position: absolute;
    left: 296px; top: 40px;
    color: var(--ink);
  }
  .contact__name {
    font-family: "Amatic SC", "Questrial", sans-serif;
    font-weight: 700;
    font-size: 30px;
    color: var(--gold-text);
    letter-spacing: 1px;
    line-height: 1;
  }
  .contact__role { font-size: 13px; margin: 4px 0 18px 6px; letter-spacing: 0.5px; }
  .contact__address { font-size: 12px; line-height: 1.35; margin-bottom: 14px; }
  .contact__line { font-size: 12px; line-height: 1.55; white-space: nowrap; }
  .contact__label { color: var(--gold-text); margin-right: 4px; }
</style>
</head>
<body>
  <section class="card card--back">
    <div class="back-pattern" role="img" aria-label="Repeating pattern of gold and green pineapples"></div>
    <div class="back-panel">
      <span class="brand-dot"></span>
      <span class="brand-name">Meadow and Rowan<br>Massage Studio</span>
    </div>
  </section>

  <section class="card card--front">
    <div class="front-pattern" role="img" aria-label="Diagonal pattern of mint pineapples on gold"></div>
    <div class="front-brand">
      <span class="brand-dot"></span>
      <span class="brand-name">Meadow and Rowan<br>Massage Studio</span>
    </div>
    <div class="contact">
      <p class="contact__name">Clara Hollis</p>
      <p class="contact__role">Artist</p>
      <p class="contact__address">Unit 8, The Linden Yard,<br>Millbrook Lane, Ashford,<br>Kent TN23 4QP</p>
      <p class="contact__line"><span class="contact__label">Phone:</span>+123 555 010 4</p>
      <p class="contact__line"><span class="contact__label">Email:</span>hello@meadowrowan.com</p>
      <p class="contact__line"><span class="contact__label">Web:</span>www.meadowrowan.com</p>
    </div>
  </section>
</body>
</html>
```